Letterhead & Business Card Design Project

Use existing logo to create a new letterhead and business card design. Looking for something clean modern using color options of black, white and gray. The green from the logo may be used lightly as an accent color.

Target Market(s)

Professional business people

Industry/Entity Type

Business

Requirements
Must have
• Business card with front and back design using existing logo.
Nice to have
• Professional presentation
Clean look
Should not have
• No oil rigs, pumpjacks or clip art.

```html
<!DOCTYPE html>
<html lang="en">
<head>
<meta charset="utf-8">
<title>Corvale Exploration – Stationery</title>
<link rel="stylesheet" href="https://fonts.googleapis.com/css2?family=Cormorant+Garamond:wght@400;600&family=Libre+Baskerville&family=Arimo&display=swap">
<style>
  :root {
    --bg: #3d3d3d;
    --paper: #ffffff;
    --ink: #1c1c1c;
    --grey: #8a8a8a;
    --card-black: #0b0b0b;
    --logo-grey: #a9a9a9;
    --green: #22a94a;
  }
  * { box-sizing: border-box; margin: 0; padding: 0; }
  html, body { width: 1200px; height: 900px; overflow: hidden; background: var(--bg); }
  .canvas { position: relative; width: 1200px; height: 900px; }

  .brand-name {
    font-family: "Cormorant Garamond", serif;
    font-weight: 400;
    letter-spacing: 0.18em;
    text-transform: uppercase;
    white-space: nowrap;
  }

  /* Letterhead */
  .letterhead {
    position: absolute; left: 70px; top: 126px;
    width: 500px; height: 648px;
    background: var(--paper);
    box-shadow: 0 6px 18px rgba(0,0,0,.35);
  }
  .letterhead .brand-name {
    position: absolute; left: 34px; top: 88px;
    font-size: 19px; color: var(--ink);
  }
  .letterhead-address {
    position: absolute; left: 290px; top: 30px; width: 180px;
    font-family: "Libre Baskerville", serif; font-size: 8px; line-height: 1.5; color: var(--ink);
  }
  .label { color: var(--grey); }
  .letter-body {
    position: absolute; left: 34px; top: 178px; width: 432px;
    font-family: "Arimo", sans-serif; font-size: 8.6px; line-height: 1.45; color: var(--ink);
  }
  .letter-body p { text-align: justify; margin-bottom: 12px; }
  .salutation { margin-bottom: 8px !important; }
  .signature-mark {
    position: absolute; left: 300px; top: 478px; width: 90px; height: 40px;
  }
  .signatory {
    position: absolute; left: 400px; top: 500px;
    font-family: "Arimo", sans-serif; font-size: 8.6px; line-height: 1.4; color: var(--ink);
  }
  .letterhead-band {
    position: absolute; left: 0; right: 0; top: 556px; height: 50px;
    background: var(--green);
    display: flex; align-items: center; justify-content: center;
    font-family: "Libre Baskerville", serif; font-size: 13px; color: var(--paper); letter-spacing: 0.02em;
  }

  /* Cards */
  .card { position: absolute; width: 480px; height: 274px; box-shadow: 0 6px 18px rgba(0,0,0,.35); }
  .card-back { left: 650px; top: 140px; background: var(--card-black); }
  .card-back .brand-name {
    position: absolute; left: 0; right: 0; top: 96px; text-align: center;
    font-size: 30px; color: var(--logo-grey);
  }
  .card-back-web {
    position: absolute; left: 0; right: 0; top: 196px; text-align: center;
    font-family: "Libre Baskerville", serif; font-size: 8px; letter-spacing: 0.25em; color: var(--grey);
  }
  .card-front { left: 650px; top: 476px; background: var(--paper); }
  .card-front .brand-name {
    position: absolute; left: 0; right: 0; top: 38px; text-align: center;
    font-size: 22px; color: var(--ink);
  }
  .card-person {
    position: absolute; left: 0; right: 0; top: 92px; text-align: center;
    font-family: "Libre Baskerville", serif; color: var(--ink);
  }
  .card-person .person-name { font-size: 12px; letter-spacing: 0.14em; text-transform: uppercase; margin-bottom: 6px; }
  .card-person .person-contact { font-size: 9.5px; line-height: 1.5; }
  .card-web-band {
    position: absolute; left: 0; right: 0; top: 174px; height: 24px;
    background: var(--green);
    display: flex; align-items: center; justify-content: center;
    font-family: "Libre Baskerville", serif; font-size: 10px; color: var(--paper);
  }
  .card-foot-band { position: absolute; left: 0; right: 0; bottom: 22px; height: 14px; background: var(--green); }
</style>
</head>
<body>
<main class="canvas">

  <section class="letterhead">
    <div class="brand-name">Corvale Exploration</div>
    <address class="letterhead-address" style="font-style:normal">
      2750 East Harlan Ave Suite 340 Millbrook,<br>
      Oklahoma 74012<br>
      <span class="label">Phone</span> 555.214.3370 <span class="label">Fax</span> 555.214.3371
    </address>

    <div class="letter-body">
      <p class="salutation">Dear Client,</p>
      <p>Lorem ipsum dolor sit amet, consectetur adipisicing elit, sed do eiusmod tempor incididunt ut labore et dolore magna aliqua. Ut enim ad minim veniam, quis nostrud exercitation ullamco laboris nisi ut aliquip ex ea commodo consequat. Duis aute irure dolor in reprehenderit in voluptate velit esse cillum dolore eu fugiat nulla pariatur. Excepteur sint occaecat cupidatat non proident, sunt in culpa qui officia deserunt mollit anim id est laborum.</p>
      <p>Lorem ipsum dolor sit amet, consectetur adipisicing elit, sed do eiusmod tempor incididunt ut labore et dolore magna aliqua. Ut enim ad minim veniam, quis nostrud exercitation ullamco laboris nisi ut aliquip ex ea commodo consequat. Duis aute irure dolor in reprehenderit in voluptate velit esse cillum dolore eu fugiat nulla pariatur. Excepteur sint occaecat cupidatat non proident, sunt in culpa qui officia deserunt mollit anim id est laborum.</p>
      <p>Lorem ipsum dolor sit amet, consectetur adipisicing elit, sed do eiusmod tempor incididunt ut labore et dolore magna aliqua. Ut enim ad minim veniam, quis nostrud exercitation ullamco laboris nisi ut aliquip ex ea commodo consequat. Duis aute irure dolor in reprehenderit in voluptate velit esse cillum dolore eu fugiat nulla pariatur. Excepteur sint occaecat cupidatat non proident, sunt in culpa qui officia deserunt mollit anim id est laborum.</p>
      <p>Lorem ipsum dolor sit amet, consectetur adipisicing elit, sed do eiusmod tempor incididunt ut labore et dolore magna aliqua. Ut enim ad minim veniam, quis nostrud exercitation ullamco laboris nisi ut aliquip ex ea commodo consequat. Duis aute irure dolor in reprehenderit in voluptate velit esse cillum dolore eu fugiat nulla pariatur. Excepteur sint occaecat cupidatat non proident, sunt in culpa qui officia deserunt mollit anim id est laborum.</p>
      <p>Lorem ipsum dolor sit amet, consectetur adipisicing elit, sed do eiusmod tempor incididunt ut labore et dolore magna aliqua. Ut enim ad minim veniam, quis nostrud exercitation ullamco laboris nisi ut aliquip ex ea</p>
    </div>

    <svg class="signature-mark" viewBox="0 0 90 40" role="img" aria-label="Handwritten signature of Daniel Reeve">
      <rect width="90" height="40" fill="#f1f1f1"/>
    </svg>
    <div class="signatory">Daniel Reeve<br>Executive manager</div>

    <div class="letterhead-band">www.corvaleexploration.com</div>
  </section>

  <section class="card card-back">
    <div class="brand-name">Corvale Exploration</div>
    <div class="card-back-web">www.corvaleexploration.com</div>
  </section>

  <section class="card card-front">
    <div class="brand-name">Corvale Exploration</div>
    <div class="card-person">
      <div class="person-name">Clara Whitmore</div>
      <div class="person-contact">
        2750 East Harlan Ave Suite 340 Millbrook,<br>
        Oklahoma 74012<br>
        <span class="label">Phone</span> 555.214.3370 <span class="label">Fax</span> 555.214.3371
      </div>
    </div>
    <div class="card-web-band">www.corvaleexploration.com</div>
    <div class="card-foot-band"></div>
  </section>

</main>
</body>
</html>
```